Bed Company needs business card

Hello, we are a bed company that makes specialized magnets for beds. We are an alternative healing company. I need a modern and upscale business card. Please incorporate my logo for the card.

Accepted file formats are AI, EPS, and Press-Ready PDFS.

Please include all fonts or convert them to outlines regardless of file type.

If you are designing the card in Photoshop the file Must be 1200dpi.

I am open to anything for the business card.  I really like all of your designs and if you want to change the color of the logo, you can.  I will be making the final selection by Friday.  Thank You for all of your designs.  Feel Free to submit different color logos if you want.  

Reason: I will make a decision Final on Friday April 20th. 2012. Good Luck and Thank you all for the designs.

Target Market(s)

My target Market is people, who are looking for alternative healing.

Industry/Entity Type

Business

Requirements
Must have
• My logo must be incorporated. The front card must have

Name
Job Title

Address
Work
Cell
Fax
email
web

Just put in fake info for the card.

The back of the card. I want the logo on the back with color. I just want it to look modern and cool.

```html
<!DOCTYPE html>
<html lang="en">
<head>
<meta charset="utf-8">
<title>Restwell Field – Business Card</title>
<link rel="stylesheet" href="https://fonts.googleapis.com/css2?family=Open+Sans:wght@400;700&display=swap">
<style>
  :root {
    --green-bright: #3ecf1c;
    --green-deep: #2a8a12;
    --green-text: #2f8a1a;
    --ink: #141414;
    --silver-light: #eef5f1;
    --silver-mid: #a9b3ae;
    --silver-dark: #5f6964;
  }
  html, body {
    margin: 0;
    padding: 0;
    width: 1200px;
    height: 783px;
    overflow: hidden;
    background: #ffffff;
  }
  .card {
    position: relative;
    width: 1200px;
    height: 783px;
    overflow: hidden;
    font-family: "Open Sans", sans-serif;
  }
  .card-texture {
    position: absolute;
    inset: 0;
    background:
      radial-gradient(ellipse 38% 42% at 52% 52%, var(--silver-light) 0%, rgba(238,245,241,0.6) 45%, rgba(238,245,241,0) 100%),
      radial-gradient(ellipse 60% 55% at 18% 30%, rgba(220,230,225,0.7) 0%, rgba(220,230,225,0) 70%),
      radial-gradient(ellipse 55% 50% at 85% 80%, rgba(215,226,220,0.6) 0%, rgba(215,226,220,0) 70%),
      linear-gradient(135deg, var(--silver-mid) 0%, var(--silver-dark) 40%, var(--silver-mid) 70%, var(--silver-dark) 100%);
  }
  .brand-square {
    position: absolute;
    left: 190px;
    top: 52px;
    width: 110px;
    height: 110px;
    background: var(--green-deep);
  }
  .brand-name {
    position: absolute;
    left: 304px;
    top: 146px;
    margin: 0;
    font-size: 99px;
    font-weight: 700;
    line-height: 1;
    letter-spacing: -0.01em;
    color: var(--green-bright);
    white-space: nowrap;
  }
  .brand-tagline {
    position: absolute;
    left: 561px;
    top: 262px;
    margin: 0;
    font-size: 32px;
    font-weight: 400;
    line-height: 1;
    letter-spacing: 0.2em;
    color: var(--green-deep);
    white-space: nowrap;
  }
  .person-name {
    position: absolute;
    left: 0;
    width: 1254px;
    top: 330px;
    margin: 0;
    text-align: center;
    font-size: 78px;
    font-weight: 400;
    letter-spacing: -0.05em;
    line-height: 1;
    color: var(--green-deep);
  }
  .person-title {
    position: absolute;
    left: 0;
    width: 1254px;
    top: 430px;
    margin: 0;
    text-align: center;
    font-size: 38px;
    letter-spacing: -0.04em;
    color: var(--ink);
  }
  .contact {
    position: absolute;
    margin: 0;
    color: var(--green-text);
    letter-spacing: -0.05em;
    white-space: nowrap;
    line-height: 1;
  }
  .contact-city { left: 136px; top: 526px; font-size: 54px; }
  .contact-phone { left: 125px; top: 602px; font-size: 50px; }
  .contact-cell { left: 797px; top: 542px; font-size: 65px; }
  .contact-email { left: 671px; top: 628px; font-size: 41px; }
</style>
</head>
<body>
  <main class="card">
    <div class="card-texture" role="img" aria-label="Silvery metallic wave texture with a soft bright glow in the centre"></div>

    <div class="brand-square"></div>
    <h1 class="brand-name">Restwell Field</h1>
    <p class="brand-tagline">Alternative Healing</p>

    <h2 class="person-name">Daniel Marsh</h2>
    <p class="person-title">Business Manager</p>

    <p class="contact contact-city">Oakridge</p>
    <p class="contact contact-phone">phone: 48213</p>
    <p class="contact contact-cell">Cell: 07352</p>
    <p class="contact contact-email">Email:team@restwell.com</p>
  </main>
</body>
</html>
```